KWT BUSINESS CARD

I'd like a new business card for the folks in my office. I recently became aware of a company that produces extra thick cards that seem to me to make excellent use of embossing. I have a logo that I like so I just need a design that uses embossing effectively, is simple and uses minimal color.

I am uploading our current logo of a tooth with a brush above it. I am also uploading another file with the words of our business. In your design please use the square version of the tooth vs. the strectched version. The original logo is the more square image but please use the words and the fonts of "Wexmoor Dental Group" and incorporate that in the design.

Industry/Entity Type

Business

Colors
ffffff

Requirements
Must have
• Logo, company name (also a part of our existing logo), employee name and title, phone number and website address. Must be simple
Nice to have
• Embossed - Maybe a solid color on the back
Should not have
• Must not be too complex or busy

```html
<!DOCTYPE html>
<html lang="en">
<head>
<meta charset="utf-8">
<title>Wexmoor Dental Group – Business Card</title>
<link rel="stylesheet" href="https://fonts.googleapis.com/css2?family=Montserrat:wght@400;600;800&display=swap">
<style>
  :root {
    --ink: #050505;
    --paper: #ffffff;
    --backdrop: #e9e7e3;
    --brand-blue: #3a3f9c;
    --brand-green: #16a34a;
    --muted: #cfcfcf;
  }
  * { box-sizing: border-box; margin: 0; padding: 0; }
  html, body { width: 1200px; height: 1023px; overflow: hidden; }
  body {
    background: var(--backdrop);
    font-family: "Montserrat", sans-serif;
    position: relative;
  }
  .card {
    position: absolute;
    width: 580px;
    height: 330px;
    border-radius: 14px;
    overflow: hidden;
    background: var(--ink);
    box-shadow: 0 10px 28px rgba(0,0,0,.28);
  }
  .card--front { left: 90px; top: 110px; }
  .card--back { left: 530px; top: 560px; }

  /* Front */
  .front-lockup {
    position: absolute;
    left: 60px; top: 90px;
    display: flex; align-items: center; gap: 26px;
  }
  .lockup-mark {
    width: 120px; height: 120px;
    background: var(--brand-blue);
    flex: none;
  }
  .lockup-name {
    color: var(--paper);
    font-weight: 800;
    font-size: 44px;
    line-height: 1.02;
    letter-spacing: 1px;
    text-transform: uppercase;
  }
  .front-url {
    position: absolute;
    right: 34px; bottom: 26px;
    color: var(--paper);
    font-size: 15px; font-weight: 600;
  }

  /* Back */
  .back-art { position: absolute; left: 0; top: 0; width: 580px; height: 330px; }
  .back-lockup {
    position: absolute;
    left: 30px; top: 44px;
    display: flex; align-items: center; gap: 12px;
  }
  .back-lockup .lockup-mark { width: 64px; height: 64px; }
  .back-lockup .lockup-name { color: var(--ink); font-size: 21px; }
  .person {
    position: absolute;
    left: 30px; bottom: 14px;
    color: var(--paper);
  }
  .person-name { font-size: 20px; font-weight: 600; letter-spacing: .5px; line-height: 1.2; }
  .person-title { font-size: 13px; color: var(--muted); line-height: 1.3; }
  .contacts {
    position: absolute;
    left: 345px; top: 170px;
    list-style: none;
    color: var(--paper);
    font-size: 12px; font-weight: 600;
  }
  .contacts li { display: flex; align-items: center; gap: 8px; margin-bottom: 12px; white-space: nowrap; }
  .contacts svg { width: 12px; height: 12px; flex: none; }
</style>
</head>
<body>

<section class="card card--front" aria-label="Card front">
  <div class="front-lockup">
    <div class="lockup-mark"></div>
    <div class="lockup-name">Wexmoor<br>Dental<br>Group</div>
  </div>
  <div class="front-url">www.wexmoordentalgroup.com</div>
</section>

<section class="card card--back" aria-label="Card back">
  <svg class="back-art" viewBox="0 0 580 330" aria-hidden="true">
    <path d="M0 0 H280 C370 70 375 195 312 255 L0 255 Z" fill="var(--brand-blue)"/>
    <path d="M0 0 H255 C342 70 350 190 290 255 L0 255 Z" fill="var(--paper)"/>
    <path d="M20 255 C150 248 280 205 325 140 C300 212 200 252 120 255 Z" fill="var(--brand-green)"/>
  </svg>
  <div class="back-lockup">
    <div class="lockup-mark"></div>
    <div class="lockup-name">Wexmoor<br>Dental<br>Group</div>
  </div>
  <div class="person">
    <div class="person-name">DANA MORRELL</div>
    <div class="person-title">office manager</div>
  </div>
  <ul class="contacts">
    <li>
      <svg viewBox="0 0 24 24"><path fill="var(--brand-green)" d="M6.6 10.8a15 15 0 0 0 6.6 6.6l2.2-2.2a1 1 0 0 1 1-.25 11.4 11.4 0 0 0 3.6.6 1 1 0 0 1 1 1V20a1 1 0 0 1-1 1A17 17 0 0 1 3 4a1 1 0 0 1 1-1h3.5a1 1 0 0 1 1 1c0 1.25.2 2.45.6 3.6a1 1 0 0 1-.25 1z"/></svg>
      555-014-2286
    </li>
    <li>
      <svg viewBox="0 0 24 24"><rect x="2" y="5" width="20" height="14" fill="none" stroke="var(--brand-green)" stroke-width="2"/><path d="M2 5l10 8 10-8" fill="none" stroke="var(--brand-green)" stroke-width="2"/></svg>
      danamorrell@email.com
    </li>
    <li>
      <svg viewBox="0 0 24 24"><circle cx="12" cy="12" r="10" fill="var(--brand-green)"/></svg>
      www.wexmoordentalgroup.com
    </li>
  </ul>
</section>

</body>
</html>
```